LOCAL TAXI SERVICE NEEDS A BANNER AD DESIGN

NEED BANNER AD DESIGN FOR TAXI SERVICE IN NJ. WE PROVIDE LOCAL AND LONG DISTANCE TRANSPORTATION. OUR MAIN BASE OF CUSTOMER GO TO THE MAJOR AIRPORTS IN THE TRI STATE AREA. I WANT TO OFFER A SPECIAL GOING TO DALMORE AIRPORT OF $35.00 WITH A COUPON CODE OF CP 12. THIS BANNER AD WILL BE USED FOR MY CHIRPLANE PAGE

Target Market(s)

PEOPLE WHO TRAVEL A LOT

Industry/Entity Type

Taxi

Font styles to use
Serif
Sans Serif

Colors
0792cd
0255a3
33a6d7
85cae6
cee9f5
ecf7fb
ffffff

Requirements
Must have
• MY COMPANY NAME: MAVIN'S TAXI

```html
<!DOCTYPE html>
<html lang="en">
<head>
<meta charset="utf-8">
<title>Mavin's Taxi – Banner Ad Designs</title>
<link rel="stylesheet" href="https://fonts.googleapis.com/css2?family=Source+Sans+3:wght@600;700&display=swap">
<style>
  :root {
    --page-bg: #ecf7fb;
    --white: #ffffff;
    --accent: #33a6d7;
    --blue-deep: #0255a3;
    --blue-bright: #0792cd;
    --panel-charcoal: #2a2a2a;
    --panel-charcoal-light: #4a4a4a;
    --panel-navy: #0b1a24;
    --panel-navy-light: #173848;
    --sky: #9aa3a8;
    --sky-dark: #5f686e;
    --field: #a08a63;
    --road: #3a3c3e;
    --logo-band: rgba(20, 20, 20, 0.78);
  }
  * { box-sizing: border-box; margin: 0; padding: 0; }
  html, body {
    width: 867px;
    height: 1200px;
    overflow: hidden;
  }
  body {
    background: var(--page-bg);
    font-family: "Source Sans 3", "Source Sans Pro", Arial, sans-serif;
    position: relative;
  }
  .banner {
    position: absolute;
    left: 35px;
    width: 798px;
    height: 419px;
    display: flex;
    box-shadow: 0 6px 18px rgba(0, 0, 0, 0.35);
  }
  .banner--charcoal { top: 44px; }
  .banner--navy { top: 577px; }

  .banner__photo {
    position: relative;
    width: 285px;
    height: 100%;
    background:
      linear-gradient(180deg, var(--sky-dark) 0%, var(--sky) 40%, #c9cbc8 52%, var(--field) 56%, var(--field) 66%, var(--road) 80%, #2c2e30 100%);
  }
  .brand {
    position: absolute;
    top: 17px;
    left: 5px;
    height: 36px;
    display: flex;
    align-items: center;
    gap: 9px;
    padding: 0 16px 0 6px;
    background: var(--logo-band);
  }
  .brand__mark {
    width: 24px;
    height: 24px;
    background: var(--blue-bright);
  }
  .brand__name {
    color: var(--white);
    font-weight: 600;
    font-size: 23px;
    letter-spacing: 0.5px;
  }

  .banner__offer {
    position: relative;
    flex: 1;
    height: 100%;
    color: var(--white);
    text-align: center;
    font-weight: 700;
  }
  .banner--charcoal .banner__offer {
    background: radial-gradient(ellipse at 50% 35%, var(--panel-charcoal-light) 0%, var(--panel-charcoal) 70%, #1f1f1f 100%);
  }
  .banner--navy .banner__offer {
    background: radial-gradient(ellipse at 50% 95%, var(--panel-navy-light) 0%, var(--panel-navy) 65%, #071118 100%);
  }
  .offer__lead {
    position: absolute;
    top: 22px;
    width: 100%;
    font-size: 29px;
    line-height: 36px;
  }
  .offer__destination {
    position: absolute;
    top: 56px;
    width: 100%;
    font-size: 46px;
    line-height: 56px;
  }
  .offer__destination .highlight { color: var(--accent); }
  .offer__label {
    position: absolute;
    width: 100%;
    font-size: 29px;
    line-height: 36px;
  }
  .offer__label--price { top: 153px; }
  .offer__label--code { top: 279px; }
  .offer__price {
    position: absolute;
    top: 186px;
    width: 100%;
    font-size: 42px;
    line-height: 52px;
    color: var(--accent);
  }
  .coupon {
    position: absolute;
    top: 332px;
    left: 150px;
    width: 216px;
    height: 67px;
    display: flex;
    align-items: center;
    justify-content: center;
    background: linear-gradient(90deg, var(--blue-deep) 0%, var(--blue-bright) 50%, var(--blue-deep) 100%);
    font-size: 42px;
    color: var(--white);
  }
</style>
</head>
<body>

  <section class="banner banner--charcoal">
    <div class="banner__photo" role="img" aria-label="Photo of a white sedan on an open road under a cloudy sky">
      <div class="brand">
        <span class="brand__mark"></span>
        <span class="brand__name">MAVIN'S TAXI</span>
      </div>
    </div>
    <div class="banner__offer">
      <p class="offer__lead">WANT TO GOING</p>
      <p class="offer__destination">DALMORE <span class="highlight">AIRPORT ?</span></p>
      <p class="offer__label offer__label--price">SPECIAL OFFER PRICE</p>
      <p class="offer__price">$35.00</p>
      <p class="offer__label offer__label--code">USE THIS COUPON CODE</p>
      <div class="coupon">CP 12</div>
    </div>
  </section>

  <section class="banner banner--navy">
    <div class="banner__photo" role="img" aria-label="Photo of a white sedan on an open road under a cloudy sky">
      <div class="brand">
        <span class="brand__mark"></span>
        <span class="brand__name">MAVIN'S TAXI</span>
      </div>
    </div>
    <div class="banner__offer" role="img" aria-label="Dark navy hexagon pattern background with offer details">
      <p class="offer__lead">WANT TO GOING</p>
      <p class="offer__destination">DALMORE <span class="highlight">AIRPORT ?</span></p>
      <p class="offer__label offer__label--price">SPECIAL OFFER PRICE</p>
      <p class="offer__price">$35.00</p>
      <p class="offer__label offer__label--code">USE THIS COUPON CODE</p>
      <div class="coupon">CP 12</div>
    </div>
  </section>

</body>
</html>
```